Business card with logo for a family psychologist

I need a business card for my private practice in the urban Chicago area as a psychologist. I see families and individuals who are going through difficult times - divorce, separation, illness, or trauma. I want to project hopefulness, competence, and caring.

Target Market(s)

Adults, other professionals - such as physicans and lawyers

Industry/Entity Type

Health Care

Contact Information for Business Card

Front should have my name and credentials; back should have location information including my email, phone

Font styles to use
Serif
Decorative
Script

Requirements
Must have
• Unique logo
Should not have
• No pictures or icons of people; no black

```html
<!DOCTYPE html>
<html lang="en">
<head>
<meta charset="utf-8">
<title>Dana Morrow, Ph.D. – Business Card</title>
<link rel="stylesheet" href="https://fonts.googleapis.com/css2?family=Source+Sans+3:wght@300;400;600;700&display=swap">
<style>
  :root {
    --brand-blue: #0754a5;
    --brand-green: #7cc45a;
    --soft-green: #c4e3b0;
    --soft-blue: #9ccbe6;
    --paper: #ffffff;
    --backdrop: #e9e7e2;
    --back-pieces: #7aa7d8;
  }
  * { box-sizing: border-box; margin: 0; padding: 0; }
  html, body {
    width: 1078px; height: 1200px; overflow: hidden;
    background: var(--backdrop);
    font-family: "Source Sans 3", "Helvetica Neue", Arial, sans-serif;
  }
  .canvas { position: relative; width: 1078px; height: 1200px; }

  .card {
    position: absolute;
    width: 774px; height: 445px;
    overflow: hidden;
    box-shadow: 0 2px 6px rgba(0,0,0,0.18);
  }

  /* Front */
  .card-front { left: 152px; top: 118px; background: var(--paper); }
  .front-band {
    position: absolute; left: 0; top: 0;
    width: 187px; height: 100%;
    background: var(--brand-blue);
  }
  .front-stripe {
    position: absolute; left: 187px; top: 0;
    width: 10px; height: 100%;
    background: var(--brand-green);
  }
  .front-mark {
    position: absolute; left: 84px; top: 66px;
    width: 206px; height: 206px; border-radius: 50%;
    background: var(--paper);
    display: flex; align-items: center; justify-content: center;
  }
  .front-mark .mark-disc {
    width: 178px; height: 178px; border-radius: 50%;
    background: var(--brand-green);
    display: flex; align-items: center; justify-content: center;
  }
  .mark-name {
    font-weight: 600; font-size: 30px; letter-spacing: 0.5px;
    color: var(--paper);
  }
  .front-identity {
    position: absolute; left: 316px; top: 149px;
    color: var(--brand-blue);
  }
  .identity-name { font-weight: 700; font-size: 25px; line-height: 32px; }
  .identity-title { font-weight: 400; font-size: 24px; line-height: 32px; }

  .corner-decor {
    position: absolute;
    width: 200px; height: 205px;
  }
  .card-front .corner-decor {
    right: 0; bottom: 0;
    background: radial-gradient(circle at 100% 100%, var(--soft-blue) 0%, var(--soft-green) 45%, rgba(255,255,255,0) 72%);
  }

  /* Back */
  .card-back { left: 149px; top: 635px; background: var(--brand-blue); color: var(--paper); }
  .card-back .corner-decor {
    right: 0; top: 0;
    background: radial-gradient(circle at 100% 0%, var(--back-pieces) 0%, rgba(122,167,216,0.55) 42%, rgba(7,84,165,0) 72%);
  }
  .back-lines { position: absolute; left: 0; top: 0; }
  .back-mark-name {
    position: absolute; left: 110px; top: 63px;
    width: 108px; height: 108px;
    display: flex; align-items: center; justify-content: center;
    font-weight: 600; font-size: 21px; color: var(--brand-blue);
  }
  .back-identity { position: absolute; left: 236px; top: 99px; }
  .back-identity .identity-name { font-size: 22px; line-height: 28px; }
  .back-identity .identity-title { font-weight: 300; font-size: 23px; line-height: 30px; }
  .contact-list {
    position: absolute; left: 201px; top: 0;
    font-weight: 300; font-size: 23px; line-height: 30px;
    list-style: none;
  }
  .contact-address { position: absolute; top: 250px; white-space: nowrap; }
  .contact-phone { position: absolute; top: 326px; white-space: nowrap; }
  .contact-email { position: absolute; top: 375px; white-space: nowrap; }
</style>
</head>
<body>
<main class="canvas">

  <section class="card card-front" aria-label="Business card front">
    <div class="front-band"></div>
    <div class="front-stripe"></div>
    <div class="front-mark">
      <div class="mark-disc"><span class="mark-name">Elmway</span></div>
    </div>
    <div class="front-identity">
      <p class="identity-name">Dana Morrow, Ph.D.</p>
      <p class="identity-title">Licensed Clinical Psychologist</p>
    </div>
    <div class="corner-decor" role="img" aria-label="Scattered puzzle piece decoration in soft green and blue"></div>
  </section>

  <section class="card card-back" aria-label="Business card back">
    <div class="corner-decor" role="img" aria-label="Scattered puzzle piece decoration in light blue"></div>

    <svg class="back-lines" width="774" height="445" viewBox="0 0 774 445" aria-hidden="true">
      <line x1="164" y1="160" x2="164" y2="445" stroke="#ffffff" stroke-width="7"/>
      <circle cx="164" cy="117" r="57" fill="#ffffff"/>
      <!-- pin -->
      <circle cx="166" cy="269" r="17" fill="#0754a5" stroke="#ffffff" stroke-width="2.5"/>
      <path d="M166 279 C160 271 159 268 159 265 a7 7 0 0 1 14 0 c0 3 -1 6 -7 14 z" fill="none" stroke="#ffffff" stroke-width="2"/>
      <circle cx="166" cy="265" r="2.5" fill="#ffffff"/>
      <!-- phone -->
      <circle cx="166" cy="338" r="17" fill="#0754a5" stroke="#ffffff" stroke-width="2.5"/>
      <path d="M160 329 l4 -1 l2 6 l-2.5 2 c1.5 3 3 4.5 6 6 l2 -2.5 l6 2 l-1 4 c-9 0 -17 -8 -16.5 -16.5 z" fill="none" stroke="#ffffff" stroke-width="1.8" stroke-linejoin="round"/>
      <!-- envelope -->
      <circle cx="166" cy="389" r="17" fill="#0754a5" stroke="#ffffff" stroke-width="2.5"/>
      <rect x="156" y="382" width="20" height="14" fill="none" stroke="#ffffff" stroke-width="1.8"/>
      <path d="M156 382 l10 8 l10 -8" fill="none" stroke="#ffffff" stroke-width="1.8"/>
    </svg>
    <div class="back-mark-name">Elmway</div>

    <div class="back-identity">
      <p class="identity-name">Dana Morrow, Ph.D.</p>
      <p class="identity-title">Licensed Clinical Psychologist</p>
    </div>

    <ul class="contact-list">
      <li class="contact-address">250 W. Lakeview Suite 810<br>Chicago, Illinois 60606</li>
      <li class="contact-phone">312-555-0148</li>
      <li class="contact-email">drdanamorrow@mail.com</li>
    </ul>
  </section>

</main>
</body>
</html>
```